stars + comments Reviews website design (similar to quarn concept)

Please refer to attached logo and wire frames
----------------------------------------------------------------------------------------------------
we are a company based in egypt, seeking a design for a website that allows user to find doctors using search and filters.
also it allows user to review this doctor through providing comment and 1 to 5 stars
i need 4 main pages designs:
1- Doctors list/favorites list
2- Doctor view
3- Add doctor (3 steps)
4- Sign-in/sign up
5- Menu design
am into the colors teal/turquoise (though am open for different opinion)
i don't want the design theme to be doctors specific
am into the school of very clean, very neat, very simple
(plombex, ruvanteo, melvoshade designs are appealing to me)

Number of Pages Required

4 page

Font styles to use
Sans Serif

Colors
00a990
33b8a4

Requirements
Must have
• website will be bilingual/ bi-directional (English and Arabic)
• designer needs to provide another copy of the design with "right to left" orientation
• interactive button animation

```html
<!DOCTYPE html>
<html lang="en">
<head>
<meta charset="utf-8">
<title>Ratevia – Favorite Doctors</title>
<link href="https://fonts.googleapis.com/css2?family=Arimo:wght@400;700&display=swap" rel="stylesheet">
<style>
  :root{
    --teal:#009a98;
    --bar:#1f1f1f;
    --icon-dark:#222222;
    --fav-red:#e8323c;
    --page-bg:#ebe8e1;
    --card-bg:#f7f6f3;
    --divider:#d6d4d0;
    --text:#333333;
    --text-strong:#1c1c1c;
    --star:#fbb40a;
    --white:#ffffff;
  }
  *{box-sizing:border-box;margin:0;padding:0}
  html,body{width:1200px;height:929px;overflow:hidden}
  body{position:relative;background:var(--page-bg);font-family:"Arimo",Arial,sans-serif;color:var(--text)}

  .site-header{position:absolute;left:0;top:0;width:1200px;height:103px;background:var(--teal)}
  .brand{position:absolute;left:105px;top:18px;font-size:50px;font-weight:700;color:var(--white);letter-spacing:0.5px;line-height:66px}
  .nav-icon{position:absolute;top:31px;width:50px;height:50px;border-radius:50%;background:var(--icon-dark);display:flex;align-items:center;justify-content:center}
  .nav-icon--home{left:522px}
  .nav-icon--fav{left:646px;background:var(--fav-red)}
  .nav-icon--add{left:772px}
  .nav-icon svg{display:block}
  .account-menu{position:absolute;left:949px;top:37px;width:121px;height:35px;border:1px solid var(--white);color:var(--white);font-size:15px;display:flex;align-items:center;justify-content:center;gap:8px}
  .caret{width:0;height:0;border-left:5px solid transparent;border-right:5px solid transparent;border-top:5px solid currentColor}

  .filter-bar{position:absolute;left:0;top:103px;width:1200px;height:76px;background:var(--bar);border-bottom:5px solid var(--white);box-shadow:0 3px 4px rgba(0,0,0,.18)}
  .filter-bar::after{content:"";position:absolute;left:0;right:0;bottom:-5px}
  .field{position:absolute;height:31px;background:var(--white);color:var(--text);font-size:15px;display:flex;align-items:center;justify-content:space-between;padding:0 8px 0 8px}
  .field .caret{color:#222}
  .field--search{left:111px;top:21px;width:171px;padding-right:6px}
  .field--spec{left:312px;top:22px;width:150px}
  .field--sub{left:490px;top:23px;width:153px;padding-left:7px}
  .field--gender{left:673px;top:23px;width:125px}
  .field--gender-b{left:829px;top:23px;width:125px;align-items:center}
  .field--gender-b .caret{align-self:flex-start;margin-top:9px}
  .field--rating{left:986px;top:23px;width:102px}

  .results-count{position:absolute;left:138px;top:221px;font-size:14px;font-weight:700;color:var(--text-strong)}

  .doctor-list{position:absolute;left:138px;top:251px;width:915px;height:606px;background:var(--card-bg);box-shadow:0 1px 4px rgba(0,0,0,.15);list-style:none}
  .doctor{position:relative;border-bottom:1px solid var(--divider)}
  .doctor:nth-child(1){height:148px}
  .doctor:nth-child(2){height:142px}
  .doctor:nth-child(3){height:145px}
  .doctor:nth-child(4){height:170px;border-bottom:none}
  .doctor__photo{position:absolute;left:26px;width:99px;height:97px}
  .doctor:nth-child(1) .doctor__photo{top:30px}
  .doctor:nth-child(2) .doctor__photo{top:23px}
  .doctor:nth-child(3) .doctor__photo{top:26px}
  .doctor:nth-child(4) .doctor__photo{top:25px}
  .photo--a{background:linear-gradient(180deg,#8f8675 0%,#a39a88 45%,#e9e9e6 100%)}
  .photo--b{background:linear-gradient(180deg,#e3c35a 0%,#c99535 55%,#7a5a3a 100%)}
  .doctor__info{position:absolute;left:140px;font-size:15px;line-height:28px;color:var(--text)}
  .doctor:nth-child(1) .doctor__info{top:36px}
  .doctor:nth-child(2) .doctor__info{top:29px}
  .doctor:nth-child(3) .doctor__info{top:32px}
  .doctor:nth-child(4) .doctor__info{top:31px}
  .doctor__rating{position:absolute;left:696px;display:flex;align-items:center;gap:0}
  .doctor:nth-child(1) .doctor__rating{top:42px}
  .doctor:nth-child(2) .doctor__rating{top:35px}
  .doctor:nth-child(3) .doctor__rating{top:38px}
  .doctor:nth-child(4) .doctor__rating{top:37px}
  .stars{display:flex;gap:1px}
  .review-count{margin-left:13px;font-size:15px;color:var(--text)}
  .fav-toggle{position:absolute;left:821px}
  .doctor:nth-child(1) .fav-toggle{top:84px}
  .doctor:nth-child(2) .fav-toggle{top:77px}
  .doctor:nth-child(3) .fav-toggle{top:80px}
  .doctor:nth-child(4) .fav-toggle{top:79px}

  .site-footer{position:absolute;left:0;top:880px;width:1256px;text-align:center;font-size:13px;color:var(--text-strong)}
</style>
</head>
<body>
<svg width="0" height="0" style="position:absolute" aria-hidden="true">
  <defs>
    <symbol id="star" viewBox="0 0 24 24"><path d="M12 1.5l3.2 6.6 7.3 1-5.3 5.1 1.3 7.2L12 18l-6.5 3.4 1.3-7.2L1.5 9.1l7.3-1z"/></symbol>
    <clipPath id="half"><rect x="0" y="0" width="12" height="24"/></clipPath>
    <symbol id="heart" viewBox="0 0 24 24"><path d="M12 21s-7.8-4.8-9.7-9.6C.9 7.9 3.2 3.8 7 3.8c2.2 0 3.8 1.2 5 3 1.2-1.8 2.8-3 5-3 3.8 0 6.1 4.1 4.7 7.6C19.8 16.2 12 21 12 21z"/></symbol>
    <symbol id="stars-45" viewBox="0 0 112 22">
      <use href="#star" x="0" y="0" width="22" height="22" fill="#fbb40a"/>
      <use href="#star" x="22.5" y="0" width="22" height="22" fill="#fbb40a"/>
      <use href="#star" x="45" y="0" width="22" height="22" fill="#fbb40a"/>
      <use href="#star" x="67.5" y="0" width="22" height="22" fill="#fbb40a"/>
      <g transform="translate(90 0) scale(0.9167)">
        <path d="M12 1.5l3.2 6.6 7.3 1-5.3 5.1 1.3 7.2L12 18l-6.5 3.4 1.3-7.2L1.5 9.1l7.3-1z" fill="none" stroke="#fbb40a" stroke-width="1.6"/>
        <path clip-path="url(#half)" d="M12 1.5l3.2 6.6 7.3 1-5.3 5.1 1.3 7.2L12 18l-6.5 3.4 1.3-7.2L1.5 9.1l7.3-1z" fill="#fbb40a"/>
      </g>
    </symbol>
  </defs>
</svg>

<header class="site-header">
  <div class="brand">Ratevia</div>
  <nav>
    <a class="nav-icon nav-icon--home" aria-label="Home">
      <svg width="34" height="30" viewBox="0 0 34 30"><path d="M17 2L2 15h4v13h8v-8h6v8h8V15h4z" fill="none" stroke="#fff" stroke-width="3" stroke-linejoin="round"/><path d="M9 16v10h4v-7h8v7h4V16l-8-7z" fill="#fff"/></svg>
    </a>
    <a class="nav-icon nav-icon--fav" aria-label="Favorites">
      <svg width="32" height="30" viewBox="0 0 24 24"><use href="#heart" fill="#fff"/></svg>
    </a>
    <a class="nav-icon nav-icon--add" aria-label="Add doctor">
      <svg width="28" height="28" viewBox="0 0 28 28"><circle cx="12" cy="8" r="5.5" fill="#fff"/><path d="M2 25c0-6 4.5-10 10-10 2 0 3.5.4 5 1.2A7 7 0 0 0 15 25z" fill="#fff"/><circle cx="21" cy="21" r="5.5" fill="#fff"/><path d="M21 18v6M18 21h6" stroke="#222" stroke-width="1.8"/></svg>
    </a>
  </nav>
  <div class="account-menu">Admin Omar <span class="caret"></span></div>
</header>

<section class="filter-bar">
  <div class="field field--search">Search
    <svg width="21" height="21" viewBox="0 0 21 21"><circle cx="8.5" cy="8.5" r="6.5" fill="none" stroke="#111" stroke-width="2.6"/><path d="M13.5 13.5l5.5 5.5" stroke="#111" stroke-width="3" stroke-linecap="round"/></svg>
  </div>
  <div class="field field--spec">Specialization <span class="caret"></span></div>
  <div class="field field--sub">Sub-specialization <span class="caret"></span></div>
  <div class="field field--gender">Gender <span class="caret"></span></div>
  <div class="field field--gender-b">Gender <span class="caret"></span></div>
  <div class="field field--rating">Rating <span class="caret"></span></div>
</section>

<main>
  <p class="results-count">15,123 Doctors</p>
  <ul class="doctor-list">
    <li class="doctor">
      <div class="doctor__photo photo--a" role="img" aria-label="Portrait photo of the doctor in a white coat"></div>
      <div class="doctor__info"><p>Karim Nassar (1 Km away)</p><p>Anesthesiogist</p><p>41 Lotus Street, Dokki</p></div>
      <div class="doctor__rating"><svg class="stars" width="112" height="22"><use href="#stars-45"/></svg><span class="review-count">(123)</span></div>
      <svg class="fav-toggle" width="30" height="30" viewBox="0 0 24 24" aria-label="Add to favorites"><use href="#heart" fill="none" stroke="#222" stroke-width="1.1"/></svg>
    </li>
    <li class="doctor">
      <div class="doctor__photo photo--b" role="img" aria-label="Portrait photo of the doctor"></div>
      <div class="doctor__info"><p>Karim Nassar (1 Km away)</p><p>Anesthesiogist</p><p>41 Lotus Street, Dokki</p></div>
      <div class="doctor__rating"><svg class="stars" width="112" height="22"><use href="#stars-45"/></svg><span class="review-count">(123)</span></div>
      <svg class="fav-toggle" width="30" height="30" viewBox="0 0 24 24" aria-label="Favorited"><use href="#heart" fill="#e8323c"/></svg>
    </li>
    <li class="doctor">
      <div class="doctor__photo photo--a" role="img" aria-label="Portrait photo of the doctor in a white coat"></div>
      <div class="doctor__info"><p>Karim Nassar (1 Km away)</p><p>Anesthesiogist</p><p>41 Lotus Street, Dokki</p></div>
      <div class="doctor__rating"><svg class="stars" width="112" height="22"><use href="#stars-45"/></svg><span class="review-count">(123)</span></div>
      <svg class="fav-toggle" width="30" height="30" viewBox="0 0 24 24" aria-label="Favorited"><use href="#heart" fill="#e8323c"/></svg>
    </li>
    <li class="doctor">
      <div class="doctor__photo photo--a" role="img" aria-label="Portrait photo of the doctor in a white coat"></div>
      <div class="doctor__info"><p>Karim Nassar (1 Km away)</p><p>Anesthesiogist</p><p>41 Lotus Street, Dokki</p></div>
      <div class="doctor__rating"><svg class="stars" width="112" height="22"><use href="#stars-45"/></svg><span class="review-count">(123)</span></div>
      <svg class="fav-toggle" width="30" height="30" viewBox="0 0 24 24" aria-label="Favorited"><use href="#heart" fill="#e8323c"/></svg>
    </li>
  </ul>
</main>

<footer class="site-footer">Copyright © 2015 The Ratevia. Powered by Pressfold and Brightloom</footer>
</body>
</html>
```